Business Card & Stationery Design for a General Contracting Company
Brenwick Contracting Limited
Tolvane Perdo
Managing Director
No 7 Marlowe Crescent, Elmsby
brenwickcontracting@quillpost.net
The Company is involved in supply and transport of aggregate materials and heavy equipment rental at present. Furthermore we recently had a project for the logo design of our Company on this website and we would like to incorporate this logo into our stationery designs and business cards. Please see the links below; Our design project; http://orders.markcraftstudio.net/contests/logo-for-a-general-contracting-company The logo chosen; http://orders.markcraftstudio.net/drafts/display/contest/512093/draft/e7d4b58213690ab1c5f93d478ee2bb718204617

```html
<!DOCTYPE html>
<html lang="en">
<head>
<meta charset="utf-8">
<title>Brenwick Contracting Limited — Business Card</title>
<link href="https://fonts.googleapis.com/css2?family=Open+Sans:wght@400;600;800&display=swap" rel="stylesheet">
<style>
  :root {
    --page-bg: #e9eaec;
    --card-white: #ffffff;
    --brand-blue: #1f5aa6;
    --brand-blue-dark: #17478a;
    --accent-red: #c4161c;
    --text-white: #ffffff;
    --divider: #6a7b93;
  }
  html, body {
    margin: 0;
    padding: 0;
    width: 1200px;
    height: 904px;
    overflow: hidden;
    background: var(--page-bg);
    font-family: "Open Sans", Arial, sans-serif;
  }
  .card {
    position: absolute;
    left: 100px;
    top: 166px;
    width: 1000px;
    height: 572px;
    border-radius: 42px;
    overflow: hidden;
    background: var(--card-white);
    box-shadow: 0 10px 30px rgba(0,0,0,0.18);
  }
  .card-waves {
    position: absolute;
    left: 0;
    top: 0;
    width: 1000px;
    height: 572px;
  }
  .brand {
    position: absolute;
    top: 178px;
    left: 0;
    width: 100%;
    display: flex;
    justify-content: center;
    align-items: center;
    gap: 18px;
  }
  .brand-dot {
    width: 46px;
    height: 46px;
    border-radius: 50%;
    background: var(--brand-blue);
  }
  .brand-name {
    font-weight: 800;
    font-size: 38px;
    letter-spacing: 0.5px;
    color: var(--brand-blue);
    text-transform: uppercase;
  }
  .person {
    position: absolute;
    top: 285px;
    left: 0;
    width: 100%;
    text-align: center;
    font-size: 24px;
    color: var(--brand-blue);
  }
  .person-name { font-weight: 600; }
  .person-sep { color: var(--divider); margin: 0 8px; }
  .person-title { font-weight: 400; }
  .contacts {
    position: absolute;
    left: 70px;
    top: 450px;
    right: 40px;
    color: var(--text-white);
    font-size: 17px;
  }
  .contact-row {
    display: flex;
    align-items: center;
    gap: 22px;
    height: 34px;
  }
  .contact-item {
    display: flex;
    align-items: center;
    gap: 7px;
    white-space: nowrap;
  }
  .icon {
    width: 18px;
    height: 18px;
    flex: none;
  }
</style>
</head>
<body>
  <div class="card">
    <svg class="card-waves" viewBox="0 0 1000 572" aria-hidden="true">
      <path d="M0,372 C300,330 700,322 1000,306 L1000,572 L0,572 Z" fill="#d9dde3"/>
      <path d="M0,378 C300,336 700,328 1000,312 L1000,572 L0,572 Z" fill="var(--accent-red)"/>
      <path d="M0,394 C300,354 700,346 1000,332 L1000,572 L0,572 Z" fill="var(--brand-blue)"/>
    </svg>

    <div class="brand">
      <div class="brand-dot"></div>
      <div class="brand-name">Brenwick Contracting Limited</div>
    </div>

    <div class="person">
      <span class="person-name">Tolvane Perdo</span><span class="person-sep">|</span><span class="person-title">Managing Director</span>
    </div>

    <div class="contacts">
      <div class="contact-row">
        <span class="contact-item">
          <svg class="icon" viewBox="0 0 18 18"><circle cx="9" cy="9" r="9" fill="#fff"/><path d="M9 3.5a3.5 3.5 0 0 0-3.5 3.5c0 2.6 3.5 7 3.5 7s3.5-4.4 3.5-7A3.5 3.5 0 0 0 9 3.5z" fill="var(--brand-blue)"/><circle cx="9" cy="7" r="1.3" fill="#fff"/></svg>
          No 7 Marlowe Crescent, Elmsby
        </span>
        <span class="contact-item">
          <svg class="icon" viewBox="0 0 18 18"><circle cx="9" cy="9" r="9" fill="#fff"/><path d="M5.5 4.5l2 0 1 2.5-1.2 1a6 6 0 0 0 2.7 2.7l1-1.2 2.5 1 0 2c-5 0.5-8.5-3-8-8z" fill="var(--brand-blue)"/></svg>
          418-3027
        </span>
        <span class="contact-item">
          <svg class="icon" viewBox="0 0 18 18"><circle cx="9" cy="9" r="9" fill="#fff"/><rect x="6" y="3.5" width="6" height="11" rx="1.2" fill="var(--brand-blue)"/><rect x="7" y="5" width="4" height="6.5" fill="#fff"/></svg>
          736-2048
        </span>
        <span class="contact-item">
          <svg class="icon" viewBox="0 0 18 18"><circle cx="9" cy="9" r="9" fill="#fff"/><rect x="4.5" y="7" width="9" height="6" rx="1" fill="var(--brand-blue)"/><rect x="6" y="4" width="6" height="3.5" fill="var(--brand-blue)"/></svg>
          529-1864
        </span>
      </div>
      <div class="contact-row">
        <span class="contact-item">
          <svg class="icon" viewBox="0 0 18 18"><circle cx="9" cy="9" r="9" fill="#fff"/><rect x="4" y="5.5" width="10" height="7" rx="1" fill="var(--brand-blue)"/><path d="M4.5 6l4.5 3.5 4.5-3.5" stroke="#fff" stroke-width="1" fill="none"/></svg>
          brenwickcontracting@quillpost.net
        </span>
        <span class="contact-item">
          <svg class="icon" viewBox="0 0 18 18"><circle cx="9" cy="9" r="9" fill="#fff"/><circle cx="9" cy="9" r="5" fill="none" stroke="var(--brand-blue)" stroke-width="1.3"/><path d="M4 9h10M9 4c-2.5 3-2.5 7 0 10M9 4c2.5 3 2.5 7 0 10" stroke="var(--brand-blue)" stroke-width="1" fill="none"/></svg>
          www.brenwickbuild.net
        </span>
      </div>
    </div>
  </div>
</body>
</html>
```